Bref créative
office materials
pain medicine
Professional
Marlene Dubovski, MD
Anesthesiology and Pain Medicine
4218 Lark Ave, Suite 307
Linden Falls, Oregon 97381
novahealclinic@mailvora.com

```html
<!DOCTYPE html>
<html lang="en">
<head>
<meta charset="utf-8">
<title>Acheflow Pain Medicine – Stationery</title>
<link rel="stylesheet" href="https://fonts.googleapis.com/css2?family=Arimo:wght@400;700&display=swap">
<style>
  :root{
    --bg:#a7a8ac;
    --paper:#ffffff;
    --blue:#2b6496;
    --green:#4d9b46;
    --ink:#3a3a3a;
    --muted:#8a8a8a;
    --fold:#cfd0d2;
  }
  *{margin:0;padding:0;box-sizing:border-box}
  html,body{width:1200px;height:763px;overflow:hidden}
  body{background:var(--bg);font-family:"Arimo",Arial,sans-serif;color:var(--ink);position:relative}

  .framed{position:absolute;background:linear-gradient(90deg,var(--blue) 0 50%,var(--green) 50% 100%)}
  .framed .sheet{position:absolute;inset:7px;background:var(--paper)}

  .brand{position:absolute;display:flex;flex-direction:column;align-items:flex-start}
  .brand-dot{border-radius:50%;background:var(--green);flex:none}
  .brand-name{font-weight:700;color:var(--blue);letter-spacing:.04em;white-space:nowrap;line-height:1}
  .brand-sub{color:var(--blue);letter-spacing:.12em;white-space:nowrap;line-height:1}
  .brand-tagline{color:var(--muted);white-space:nowrap;line-height:1}

  .brand--lg .brand-dot{width:26px;height:26px;margin:0 0 6px 40px}
  .brand--lg .brand-name{font-size:22px}
  .brand--lg .brand-sub{font-size:8px;margin-top:3px}
  .brand--lg .brand-tagline{font-size:5px;margin-top:3px}
  .brand--sm .brand-dot{width:18px;height:18px;margin:0 0 4px 28px}
  .brand--sm .brand-name{font-size:15px}
  .brand--sm .brand-sub{font-size:6px;margin-top:2px}
  .brand--sm .brand-tagline{font-size:4px;margin-top:2px}

  .contact{position:absolute;font-size:8px;line-height:1.45;color:var(--ink)}
  .email{position:absolute;font-size:8px;color:var(--ink);white-space:nowrap}

  /* letterhead */
  .letterhead{left:24px;top:36px;width:535px;height:684px}
  .letterhead .brand{left:24px;top:8px}
  .letterhead .contact{left:24px;bottom:22px}
  .letterhead .email{left:396px;bottom:24px}

  /* business card */
  .card{left:10px;top:312px;width:262px;height:126px;z-index:2}
  .card .sheet{inset:4px}
  .card .brand{left:10px;top:10px}
  .card .contact{left:176px;top:58px;font-size:4.5px}
  .card .holder{position:absolute;left:10px;top:82px;font-size:4.5px;line-height:1.4}

  /* envelope back */
  .envelope-back{position:absolute;left:576px;top:96px;width:593px;height:271px;background:var(--paper)}
  .envelope-back svg{position:absolute;inset:0}
  .envelope-back .brand{left:50%;top:30px;transform:translateX(-50%);align-items:center}
  .envelope-back .brand-dot{margin:0 0 4px 0}

  /* envelope front */
  .envelope-front{left:576px;top:413px;width:593px;height:276px}
  .envelope-front .brand{left:24px;top:8px}
  .envelope-front .contact{left:24px;top:180px}
  .envelope-front .email{left:281px;top:196px}
</style>
</head>
<body>

<section class="framed letterhead">
  <div class="sheet">
    <div class="brand brand--lg">
      <span class="brand-dot"></span>
      <span class="brand-name">ACHEFLOW</span>
      <span class="brand-sub">Pain Medicine</span>
      <span class="brand-tagline">complete care for lasting relief and better living</span>
    </div>
    <div class="contact">
      <b>P:</b> 555-014-2210<br>
      <b>F:</b> 555-014-2287<br>
      <b>A:</b> 4218 Lark Ave, Suite 307<br>
      Linden Falls, Oregon 97381
    </div>
    <div class="email"><b>E:</b> novahealclinic@mailvora.com</div>
  </div>
</section>

<section class="framed card">
  <div class="sheet">
    <div class="brand brand--sm">
      <span class="brand-dot"></span>
      <span class="brand-name">ACHEFLOW</span>
      <span class="brand-sub">Pain Medicine</span>
      <span class="brand-tagline">complete care for lasting relief and better living</span>
    </div>
    <div class="contact">
      <b>P:</b> 555-014-2210<br>
      <b>F:</b> 555-014-2287<br>
      <b>A:</b> 4218 Lark Ave, Suite 307<br>
      Linden Falls, Oregon 97381<br>
      <b>E:</b> novahealclinic@mailvora.com
    </div>
    <div class="holder"><b>Marlene Dubovski, MD</b><br>Anesthesiology and Pain Medicine</div>
  </div>
</section>

<section class="envelope-back">
  <svg width="593" height="271" viewBox="0 0 593 271" aria-hidden="true">
    <polyline points="0,0 296,132 593,0" fill="none" stroke="var(--fold)" stroke-width="1.5"/>
  </svg>
  <div class="brand brand--sm">
    <span class="brand-dot"></span>
    <span class="brand-name">ACHEFLOW</span>
  </div>
</section>

<section class="framed envelope-front">
  <div class="sheet">
    <div class="brand brand--lg">
      <span class="brand-dot"></span>
      <span class="brand-name">ACHEFLOW</span>
      <span class="brand-sub">Pain Medicine</span>
      <span class="brand-tagline">complete care for lasting relief and better living</span>
    </div>
    <div class="contact">
      <b>P:</b> 555-014-2210<br>
      <b>F:</b> 555-014-2287<br>
      <b>A:</b> 4218 Lark Ave, Suite 307<br>
      Linden Falls, Oregon 97381
    </div>
    <div class="email"><b>E:</b> novahealclinic@mailvora.com</div>
  </div>
</section>

</body>
</html>
```